High End Notary Service Business Card Design

Want a professional and elegant/luxurious business card that is clean and simple in the design. A notary is a trusted professional that helps people sign very important documents. The card should be in alignment with this service provided.

Most of the time, service will be for the purchase of a home or refinance of a mortgage

There is NO LOGO. This is aesthetic. A look and feel. Conveying professionalism and concierge level of service.

Target Market(s)

Other business professionals, Lawyers, Escrow Officers, Loan Officers

Industry/Entity Type

Legal

Contact Information for Business Card

This will be a one-sided business card

Colors
35a7d7
3176b5
85cae6
d3a5cc
b868aa
ffffff
0356a4

Requirements
Must have
• Lorena T. Mirabel-Hodgkins
Notary Public

642-871-3094
MirabelSigningDesk@Wexmail.com
Nice to have
• Headshot photo below. Convey the aspect of signing documents. No black cards. Preference is shades of blue: light blue, navy, aqua, gold, white, or lavendar, etc.
Should not have
• No scales or legal scales.

```html
<!DOCTYPE html>
<html lang="en">
<head>
<meta charset="utf-8">
<title>Lorena T. Mirabel-Hodgkins — Notary Public</title>
<link rel="stylesheet" href="https://fonts.googleapis.com/css2?family=Archivo:wght@700;800;900&display=swap">
<style>
  :root {
    --marble-light: #ffffff;
    --marble-vein: #e6e9ee;
    --marble-shade: #f1f3f6;
    --frame-gold: #a5804f;
    --ink: #0b0b0b;
    --portrait-bg: #c9c8c3;
    --portrait-warm: #b98a66;
    --accent-soft: rgba(190, 150, 105, 0.55);
    --accent-fade: rgba(190, 150, 105, 0);
  }
  html, body {
    margin: 0;
    padding: 0;
    width: 1200px;
    height: 686px;
    overflow: hidden;
    background: var(--marble-light);
  }
  .card {
    position: relative;
    width: 1200px;
    height: 686px;
    overflow: hidden;
    background:
      radial-gradient(ellipse at 75% 20%, var(--marble-shade) 0%, transparent 55%),
      radial-gradient(ellipse at 40% 85%, var(--marble-vein) 0%, transparent 45%),
      linear-gradient(135deg, var(--marble-light) 0%, var(--marble-shade) 50%, var(--marble-light) 100%);
    font-family: "Archivo", "Arial Black", sans-serif;
    color: var(--ink);
  }
  .card__frame {
    position: absolute;
    left: 25px;
    top: 32px;
    width: 1150px;
    height: 623px;
    box-sizing: border-box;
    border: 3px solid var(--frame-gold);
  }
  .card__portrait {
    position: absolute;
    left: -126px;
    top: 59px;
    width: 560px;
    height: 560px;
    border-radius: 50%;
    background: radial-gradient(circle at 60% 42%, var(--portrait-warm) 0%, #cfb49a 32%, var(--portrait-bg) 62%);
  }
  .card__accent-image {
    position: absolute;
    left: 815px;
    top: 549px;
    width: 360px;
    height: 58px;
    background: linear-gradient(90deg, var(--accent-fade) 0%, var(--accent-soft) 45%, var(--accent-soft) 100%);
  }
  .details {
    position: absolute;
    left: 518px;
    top: 242px;
  }
  .details__name {
    margin: 0;
    font-size: 41px;
    font-weight: 900;
    line-height: 1;
    letter-spacing: 0.2px;
  }
  .details__title {
    margin: 10px 0 0 1px;
    font-size: 22px;
    font-weight: 800;
    line-height: 1;
  }
  .details__rule {
    width: 57px;
    height: 5px;
    margin: 20px 0 0 3px;
    background: var(--ink);
  }
  .contact {
    list-style: none;
    margin: 24px 0 0 0;
    padding: 0;
  }
  .contact__item {
    display: flex;
    align-items: center;
    font-weight: 800;
  }
  .contact__item--phone {
    font-size: 32px;
    height: 48px;
  }
  .contact__item--email {
    font-size: 28px;
    height: 48px;
    margin-top: 12px;
  }
  .contact__icon {
    width: 36px;
    flex: 0 0 36px;
    margin-right: 15px;
  }
</style>
</head>
<body>
  <main class="card">
    <div class="card__portrait" role="img" aria-label="Headshot portrait of the notary"></div>
    <div class="card__frame"></div>
    <div class="card__accent-image" role="img" aria-label="Gold fountain pen resting in the lower corner"></div>

    <section class="details">
      <h1 class="details__name">Lorena T. Mirabel-Hodgkins</h1>
      <p class="details__title">Notary Public</p>
      <div class="details__rule"></div>
      <ul class="contact">
        <li class="contact__item contact__item--phone">
          <svg class="contact__icon" viewBox="0 0 36 36" aria-hidden="true">
            <path d="M8 5c2-1 3 0 4 2l2 5c1 2 0 3-1 4l-2 1c1 3 4 6 7 7l1-2c1-1 2-2 4-1l5 2c2 1 3 2 2 4l-1 2c-1 2-3 3-6 2C14 29 7 22 5 13c-1-3 0-5 2-7z" fill="#0b0b0b"/>
            <path d="M21 5a10 10 0 0 1 10 10M21 10a5 5 0 0 1 5 5" fill="none" stroke="#0b0b0b" stroke-width="2.5" stroke-linecap="round"/>
          </svg>
          <span>642-871-3094</span>
        </li>
        <li class="contact__item contact__item--email">
          <svg class="contact__icon" viewBox="0 0 36 26" aria-hidden="true">
            <rect x="0" y="0" width="36" height="26" rx="2" fill="#0b0b0b"/>
            <path d="M2 3l16 12L34 3" fill="none" stroke="#ffffff" stroke-width="2.5"/>
          </svg>
          <span>MirabelSigningDesk@Wexmail.com</span>
        </li>
      </ul>
    </section>
  </main>
</body>
</html>
```